TOR Capital Allies LLC a High Risk Big Rewards company for Rich Young Entrepreneurs

We would like a very modern, powerful in the eyes of our customers, modern, minimalist feel, financial gain. this business card is for young Rich entrepreneurs who want to invest money into High Risk, Big Rewards Businesses. The card Should sell the business!! let your creativity go Wild! I pick most of the designers for this project because of your BOLD Designs, I would like this card to be Bold, Modern, Minimalist, use as many effects in your graphic Artist Mind, Do not let the Financial sound of this business to make you think Conservative that's the last thing we are! if you have a lot of money and you want to play a risky market call US
Updates

Project Deadline Extended
Reason: have not received, enough designs to choose 1st and second place, sure I have received over 100 designs but it seems most designers are submitting every card they have ever made before and calling it mine, please we are looking for fresh ideas please!

Target Market(s)

Private Risky Investors

Industry/Entity Type

Financial

Contact Information for Business Card

powerful in the eyes of our customers,modern, minimalist feel

Font styles to use
Other font styles liked:
• Modern feeling fonts

Requirements
Must have
• The Company Name is TOR Capital Allies LLC and it must be on the CARD
• My Name, title, Cell , email
• Dalton Fairweather G.E.D.
• Managing Member
• 404.658.1937
• dalton@torcapitalallies.example
Nice to have
• try a black thick plastic card with round corners with Dalton Fairweather GED (make sure GED is smaller than name) just on one side of the card, and my phone number with out the icons and email on the other side, this card should look like a exclusive credit card or exclusive VIP card, something you would never loose

```html
<!DOCTYPE html>
<html lang="en">
<head>
<meta charset="utf-8">
<title>TOR Capital Allies LLC — Dalton Fairweather</title>
<link rel="stylesheet" href="https://fonts.googleapis.com/css2?family=Montserrat:wght@300;500;900&display=swap">
<style>
  :root {
    --page: #ffffff;
    --card: #000000;
    --ink: #ffffff;
    --company: #3a3a3a;
  }
  html, body {
    margin: 0;
    padding: 0;
    width: 1200px;
    height: 686px;
    overflow: hidden;
    background: var(--page);
  }
  .business-card {
    display: block;
    width: 1200px;
    height: 686px;
  }
  .card-face { fill: var(--card); }
  .company-name {
    font-family: "Montserrat", sans-serif;
    font-weight: 300;
    letter-spacing: 3px;
    fill: var(--company);
  }
  .holder-first,
  .holder-last {
    font-family: "Montserrat", sans-serif;
    font-weight: 900;
    fill: var(--ink);
  }
  .holder-credential {
    font-family: "Montserrat", sans-serif;
    font-weight: 500;
    fill: var(--ink);
  }
</style>
</head>
<body>
<svg class="business-card" viewBox="0 0 1200 686" xmlns="http://www.w3.org/2000/svg">
  <rect class="card-face" x="0" y="0" width="1200" height="686" rx="46" ry="46"/>

  <text class="holder-first" x="80" y="343" font-size="210"
        textLength="1046" lengthAdjust="spacingAndGlyphs">DALTON</text>
  <text class="holder-last" x="43" y="457" font-size="132"
        textLength="1117" lengthAdjust="spacingAndGlyphs">FAIRWEATHER</text>
  <text class="holder-credential" x="600" y="535" font-size="56"
        text-anchor="middle">GED</text>

  <text class="company-name" x="1140" y="640" font-size="22"
        text-anchor="end">TOR CAPITAL ALLIES LLC</text>
</svg>
</body>
</html>
```